International gaming entertainment company is looking for an innovative Power Point design *

We are looking for a Power Point design for potential international investors, partners and customers in the gaming industry, meaning that a reference to internationality and gaming should become apparent.
The template should be in a reduced and clear style with a combination of innovation and tradition. It should be adaptive and suitable for various applications (tables, shapes and diagrams).
The color scheme of our company are various shades of gray and burgundy (wine-red), however as for the design in question, we are open to other meaningful suggestions (no garish colors).
Updates

Noch kein Design dabei, dass uns 100%ig überzeugt

Target Market(s)

International investors and partners in the gaming industry

Font styles to use
Serif
Sans Serif
Other font styles liked:
• Interstate

Requirements
Must have
• Clear lines
Modern
Footer line with room for classification (eg Confidential, Public) and page number

```html
<!DOCTYPE html>
<html lang="en">
<head>
<meta charset="utf-8">
<title>Meridian Gaming International – Presentation Template</title>
<link href="https://fonts.googleapis.com/css2?family=Roboto:wght@300;400;500;700&family=Roboto+Condensed:wght@400;700&family=Oswald:wght@700&display=swap" rel="stylesheet">
<style>
:root{
  --red:#c8101d;
  --red-dark:#8e0a13;
  --ink:#262626;
  --gray:#8b9097;
  --gray-mid:#5f646b;
  --line:#d7d9dd;
  --paper:#f5f6f8;
  --canvas:#e9ebee;
  --white:#ffffff;
}
*{box-sizing:border-box;margin:0;padding:0}
html,body{width:1200px;height:4526px;overflow:hidden}
body{background:var(--canvas);font-family:"Roboto",sans-serif;color:var(--ink);position:relative}
.slide{position:absolute;width:562px;height:316px;background:var(--paper);overflow:hidden;box-shadow:0 1px 3px rgba(0,0,0,.12)}
.col-l{left:23px}.col-r{left:615px}
.a{position:absolute}
.topline{position:absolute;top:0;left:0;right:0;height:2px;background:var(--line)}
.topline::before{content:"";position:absolute;left:0;top:0;width:120px;height:2px;background:var(--red)}
.title{position:absolute;left:26px;top:16px;font-family:"Roboto Condensed",sans-serif;font-size:17px;font-weight:400;text-transform:uppercase;color:var(--ink)}
.title.red{color:var(--red)}
.ft{position:absolute;left:22px;right:22px;bottom:12px;height:18px;display:flex;align-items:center;gap:14px;border-bottom:1px solid var(--line)}
.ft-mark{font-size:10px;font-weight:700;color:var(--red);letter-spacing:.5px}
.ft-url{font-size:6px;letter-spacing:2.4px;color:var(--gray);text-transform:uppercase}
.ft-no{margin-left:auto;font-size:7px;color:var(--gray);border-bottom:2px solid var(--red);padding:0 4px 2px}
.body{font-size:7.4px;line-height:1.6;color:var(--gray-mid)}
.tiny{font-size:6px;line-height:1.5;color:var(--gray-mid)}
.ic{position:absolute;width:30px;height:30px;background:var(--red);display:flex;align-items:center;justify-content:center}
.ic svg{width:16px;height:16px;fill:var(--white)}
.wordmark{font-family:"Roboto",sans-serif;font-weight:700;letter-spacing:2px;text-transform:uppercase}
.photo{position:absolute}
.cover .band-top{position:absolute;left:0;top:0;right:0;height:20px;background:var(--red)}
.cover .band-bot{position:absolute;left:0;bottom:0;right:0;height:64px;background:var(--red)}
.mark-disc{position:absolute;border-radius:50%;background:var(--white);display:flex;align-items:center;justify-content:center}
.social{position:absolute;display:flex;gap:5px}
.social span{width:10px;height:10px;border:1px solid var(--white);border-radius:50%}
.sec-tag{position:absolute;left:408px;top:30px;width:114px;height:18px;background:var(--red);color:var(--white);font-size:8px;display:flex;align-items:center;justify-content:center;letter-spacing:.5px}
.sec-word{position:absolute;left:30px;top:48px;font-family:"Oswald",sans-serif;font-weight:700;font-size:104px;line-height:1;letter-spacing:6px;color:#d8dbe0}
.sec-rule{position:absolute;left:337px;top:253px;width:185px;height:2px;background:var(--red)}
.sec-name{position:absolute;right:40px;top:264px;font-family:"Roboto Condensed",sans-serif;color:var(--red);font-size:18px}
.tbl{position:absolute;left:61px;top:83px;border-collapse:separate;border-spacing:2px;font-size:7px}
.tbl td,.tbl th{height:16px;padding:0 6px;text-align:center;color:var(--gray-mid);background:#e7e9ec}
.tbl th{background:var(--red);color:var(--white);font-weight:400}
.tbl th.blank{background:transparent}
.tbl td.lab{background:var(--red);color:var(--white);width:78px}
.bar{position:absolute;height:4px;background:#d9dbdf}
.bar i{position:absolute;left:0;top:0;height:4px;background:var(--red)}
</style>
</head>
<body>

<section class="slide col-l cover" style="top:32px;background:var(--white)">
  <div class="band-top"></div>
  <div class="band-bot"></div>
  <div class="mark-disc" style="left:330px;top:34px;width:250px;height:250px"><span class="wordmark" style="color:var(--red);font-size:26px">Meridian</span></div>
  <div class="a" style="left:22px;top:130px;font-size:22px;font-weight:300;letter-spacing:.5px">INTERNATIONAL</div>
  <div class="a" style="left:22px;top:156px;font-size:22px;font-weight:700">GAMING ENTERTAINMENT</div>
  <div class="a" style="left:22px;top:188px;font-size:7px;letter-spacing:3.5px;font-weight:700">PRESENTATION TEMPLATE</div>
  <div class="social" style="left:26px;top:290px"><span></span><span></span><span></span></div>
</section>

<section class="slide col-r" style="top:32px;background:var(--red)">
  <div class="a" style="left:0;top:0;right:0;height:20px;background:var(--white)"></div>
  <div class="a" style="left:22px;top:130px;color:var(--white);font-size:22px;font-weight:300">MASTER <b style="font-weight:700">SLIDE</b></div>
  <div class="a" style="left:22px;top:156px;color:var(--white);font-size:22px;font-weight:700">PRESENTATION</div>
  <div class="a" style="left:22px;top:188px;color:var(--white);font-size:7px;letter-spacing:3px;font-weight:700">2020</div>
  <div class="a" style="left:22px;top:206px;width:30px;height:2px;background:var(--white)"></div>
  <div class="mark-disc" style="left:338px;top:70px;width:200px;height:200px"><span class="wordmark" style="color:var(--red);font-size:22px">Meridian</span></div>
</section>

<section class="slide col-l" style="top:378px">
  <div class="topline"></div><h2 class="title red">Agenda</h2>
  <ul class="a" style="left:74px;top:88px;list-style:none;font-size:8px;line-height:18px;color:var(--ink)">
    <li><span style="color:var(--red)">• </span>Introduction</li>
    <li><span style="color:var(--red)">• </span>About Us</li>
    <li><span style="color:var(--red)">• </span>Welcome Message</li>
    <li><span style="color:var(--red)">• </span>Company</li>
    <li><span style="color:var(--red)">• </span>Management</li>
    <li><span style="color:var(--red)">• </span>Operations</li>
    <li><span style="color:var(--red)">• </span>Careers</li>
    <li><span style="color:var(--red)">• </span>Info-graphic Charts</li>
    <li><span style="color:var(--red)">• </span>Contact Us</li>
  </ul>
  <div class="photo" role="img" aria-label="Photo of stacked casino chips and red dice" style="left:285px;top:67px;width:264px;height:153px;border-radius:50%;background:linear-gradient(135deg,#7a1a1f,#3a2a2c 60%,#2a2b2e)"></div>
  <footer class="ft"><span class="ft-mark">Meridian</span><span class="ft-url">www.meridiangaming-intl.com</span><span class="ft-no">2</span></footer>
</section>

<section class="slide col-r" style="top:378px">
  <div class="topline"></div><h2 class="title">About Us</h2>
  <div class="a" style="left:21px;top:47px;width:134px;height:222px;background:var(--red);color:var(--white);padding:24px 0 0 22px">
    <div style="font-size:26px;font-weight:300;line-height:1">3,800</div><div style="font-size:5px;letter-spacing:1px;margin:2px 0 16px 4px">GAMING MACHINES</div>
    <div style="font-size:26px;font-weight:300;line-height:1">23</div><div style="font-size:5px;letter-spacing:1px;margin:2px 0 16px 4px">LANDBASED CASINOS</div>
    <div style="font-size:26px;font-weight:300;line-height:1">270</div><div style="font-size:5px;letter-spacing:1px;margin:2px 0 0 4px">GAMING TABLES</div>
  </div>
  <p class="a body" style="left:211px;top:84px;width:310px">Lorem ipsum dolor sit amet, consectetuer adipiscing elit, sed diam nonummy nibh euismod tincidunt ut laoreet dolore magna aliquam erat volutpat. Ut wisi enim ad minim veniam, quis nostrud exerci tation ullamcorper suscipit lobortis nisl ut aliquip ex ea commodo consequat.</p>
  <p class="a body" style="left:211px;top:170px;width:310px">Lorem ipsum dolor sit amet, consectetuer adipiscing elit, sed diam nonummy nibh euismod tincidunt ut laoreet dolore magna aliquam erat volutpat. Ut wisi enim ad minim veniam, quis nostrud exerci tation ullamcorper suscipit lobortis nisl ut aliquip ex ea commodo consequat.</p>
  <footer class="ft"><span class="ft-mark">Meridian</span><span class="ft-url">www.meridiangaming-intl.com</span><span class="ft-no">3</span></footer>
</section>

<section class="slide col-l" style="top:723px">
  <div class="topline"></div><h2 class="title">What We Do</h2>
  <div class="a" style="left:28px;top:90px;width:28px;height:28px;border:2px solid var(--gray);border-radius:50%"></div>
  <p class="a body" style="left:25px;top:132px;width:178px;text-align:justify">Lorem ipsum dolor sit amet, consectetuer adipiscing elit, sed diam nonummy nibh euismod tincidunt ut laoreet dolore magna aliquam erat volutpat. Ut wisi enim ad minim veniam, quis nostrud exerci tation ullamcorper suscipit lobortis nisl ut aliquip ex ea commodo consequat.</p>
  <div class="photo" role="img" aria-label="Black and white photo of casino chips and playing cards" style="left:223px;top:51px;width:92px;height:216px;background:linear-gradient(160deg,#3a3a3a,#9a9a9a 50%,#2c2c2c)"></div>
  <div class="a" style="left:351px;top:82px;font-size:8px;font-weight:700;color:var(--red)">Our Core Values:</div>
  <div class="ic" style="left:367px;top:112px"><svg viewBox="0 0 16 16"><path d="M8 1 14 8 8 15 2 8z"/></svg></div>
  <div class="ic" style="left:476px;top:112px"><svg viewBox="0 0 16 16"><path d="M8 1C5 5 2 7 2 10a3 3 0 0 0 5 2l-1 3h4l-1-3a3 3 0 0 0 5-2c0-3-3-5-6-9z"/></svg></div>
  <div class="ic" style="left:367px;top:196px"><svg viewBox="0 0 16 16"><circle cx="8" cy="4.5" r="3"/><circle cx="4.5" cy="9.5" r="3"/><circle cx="11.5" cy="9.5" r="3"/><path d="M7 9h2l1 6H6z"/></svg></div>
  <div class="ic" style="left:476px;top:196px"><svg viewBox="0 0 16 16"><path d="M8 15 2 8.5A3.5 3.5 0 0 1 8 4a3.5 3.5 0 0 1 6 4.5z"/></svg></div>
  <div class="a tiny" style="left:362px;top:148px">Lorem ipsum</div><div class="a tiny" style="left:471px;top:148px">Lorem ipsum</div>
  <div class="a tiny" style="left:362px;top:232px">Lorem ipsum</div><div class="a tiny" style="left:471px;top:232px">Lorem ipsum</div>
  <footer class="ft"><span class="ft-mark">Meridian</span><span class="ft-url">www.meridiangaming-intl.com</span><span class="ft-no">4</span></footer>
</section>

<section class="slide col-r" style="top:723px">
  <div class="topline"></div><h2 class="title red">Four Decades of Success</h2>
  <div class="photo" role="img" aria-label="Illustration of a magnifying glass over a red card-suit icon" style="left:79px;top:69px;width:167px;height:193px;background:linear-gradient(150deg,#e4ded6,#cbbfb1 55%,#8f8a86)"></div>
  <p class="a body" style="left:281px;top:100px;width:246px">Lorem ipsum dolor sit amet, consectetuer adipiscing elit, sed diam nonummy nibh euismod tincidunt ut laoreet dolore magna aliquam erat volutpat. Ut wisi enim ad minim veniam, quis nostrud exerci tation ullamcorper suscipit lobortis nisl ut aliquip ex ea commodo consequat.</p>
  <div class="a" style="left:281px;top:232px;width:105px;height:18px;border-radius:9px;background:var(--red);color:var(--white);font-size:6.5px;letter-spacing:1.5px;font-weight:700;display:flex;align-items:center;justify-content:center">LEARN MORE</div>
  <footer class="ft"><span class="ft-mark">Meridian</span><span class="ft-url">www.meridiangaming-intl.com</span><span class="ft-no">5</span></footer>
</section>

<section class="slide col-l" style="top:1069px;background:var(--white)">
  <div class="sec-tag">SECTION 01</div>
  <div class="sec-word">COMPANY</div>
  <div class="ic" style="left:47px;top:188px;width:35px;height:35px"><svg viewBox="0 0 16 16"><path d="M2 14V6l3-2v10zm4 0V3l4-2v13zm5 0V5l3 2v7z"/></svg></div>
  <div class="a" style="left:100px;top:180px;width:1px;height:56px;background:var(--line)"></div>
  <p class="a body" style="left:114px;top:183px;width:408px">Lorem ipsum dolor sit amet, consectetuer adipiscing elit, sed diam nonummy nibh euismod tincidunt ut laoreet dolore magna aliquam erat volutpat. Ut wisi enim ad minim veniam, quis nostrud exerci tation ullamcorper suscipit lobortis nisl ut aliquip ex ea commodo consequat. Duis autem vel eum iriure dolor in hendrerit in vulputate velit esse molestie consequat.</p>
  <div class="sec-rule"></div><div class="sec-name">COMPANY</div>
</section>

<section class="slide col-r" style="top:1069px">
  <div class="topline"></div><h2 class="title">Bar Chart</h2>
  <svg class="a" style="left:16px;top:84px" width="320" height="170" viewBox="0 0 320 170" font-family="Roboto,sans-serif" font-size="5" fill="#8b9097">
    <g stroke="#e1e3e6" stroke-width=".6"><line x1="20" y1="10" x2="315" y2="10"/><line x1="20" y1="36" x2="315" y2="36"/><line x1="20" y1="62" x2="315" y2="62"/><line x1="20" y1="88" x2="315" y2="88"/><line x1="20" y1="114" x2="315" y2="114"/><line x1="20" y1="140" x2="315" y2="140"/></g>
    <text x="6" y="12">100</text><text x="8" y="38">80</text><text x="8" y="64">60</text><text x="8" y="90">40</text><text x="8" y="116">20</text><text x="10" y="142">0</text>
    <g fill="#c7cacf"><rect x="30" y="10" width="10" height="130"/><rect x="72" y="23" width="10" height="117"/><rect x="114" y="30" width="10" height="110"/><rect x="156" y="10" width="10" height="130"/><rect x="198" y="23" width="10" height="117"/><rect x="240" y="36" width="10" height="104"/><rect x="282" y="10" width="10" height="130"/></g>
    <g fill="#c8101d"><rect x="42" y="49" width="10" height="91"/><rect x="84" y="42" width="10" height="98"/><rect x="126" y="88" width="10" height="52"/><rect x="168" y="17" width="10" height="123"/><rect x="210" y="55" width="10" height="85"/><rect x="252" y="62" width="10" height="78"/><rect x="294" y="17" width="10" height="123"/></g>
    <g fill="#7c7c7c"><text x="36" y="152">Sun</text><text x="77" y="152">Mon</text><text x="120" y="152">Tu</text><text x="161" y="152">We</text><text x="204" y="152">Th</text><text x="246" y="152">Fr</text><text x="288" y="152">Sa</text></g>
    <g fill="#555" font-size="4.5"><text x="31" y="7">100</text><text x="43" y="46">70</text><text x="73" y="20">90</text><text x="85" y="39">75</text><text x="115" y="27">85</text><text x="127" y="85">40</text></g>
  </svg>
  <div class="a" style="left:362px;top:49px;width:200px;height:218px;background:var(--red);color:var(--white);padding:38px 24px 0 28px">
    <div style="font-size:14px;font-weight:500;margin-bottom:12px">LOREM IPSUM</div>
    <p style="font-size:7px;line-height:1.75;text-align:justify">Lorem ipsum dolor sit amet, consectetuer adipiscing elit, sed diam nonummy nibh euismod tincidunt ut laoreet dolore magna aliquam erat volutpat. Ut wisi enim ad minim veniam, quis nostrud exerci tation ullamcorper suscipit lobortis nisl ut aliquip ex ea commodo consequat.</p>
  </div>
  <div class="a" style="left:508px;top:40px;width:28px;height:28px;border-radius:50%;background:var(--white);border:2px solid var(--red)"></div>
  <footer class="ft" style="right:222px"><span class="ft-mark">Meridian</span><span class="ft-url">www.meridiangaming-intl.com</span></footer>
  <div class="a ft-no" style="left:522px;top:286px;font-size:7px;color:var(--white);border-color:var(--white)">7</div>
</section>

<section class="slide col-l" style="top:1414px">
  <div class="topline"></div><h2 class="title">Pie Chart</h2>
  <div class="a" style="left:86px;top:52px;font-size:7px;color:var(--ink)">Your Text here</div>
  <svg class="a" style="left:47px;top:65px" width="134" height="134" viewBox="0 0 134 134">
    <circle cx="67" cy="67" r="67" fill="#c8101d"/>
    <path d="M67 67 L67 0 A67 67 0 0 1 130.7 46.3 Z" fill="#2d2d2d" transform="rotate(10 67 67)"/>
    <path d="M67 67 L67 0 A67 67 0 0 0 -0.3 64 Z" fill="#dfe1e4" transform="rotate(10 67 67) rotate(40 67 67)"/>
    <text x="58" y="40" font-size="12" fill="#444" font-family="Roboto">22%</text>
    <text x="88" y="78" font-size="12" fill="#fff" font-family="Roboto">18%</text>
    <text x="20" y="95" font-size="12" fill="#fff" font-family="Roboto">60%</text>
  </svg>
  <div class="a" style="left:232px;top:109px;width:53px;height:50px;background:#555;color:var(--white);font-size:12px;display:flex;align-items:center;justify-content:center">10%</div>
  <div class="a" style="left:232px;top:161px;width:53px;height:50px;background:#b9bcc1;color:var(--white);font-size:12px;display:flex;align-items:center;justify-content:center">8%</div>
  <div class="a tiny" style="left:80px;top:243px;font-size:5px">● 1st Qtr &nbsp; ● 2nd Qtr &nbsp; ● 3rd Qtr &nbsp; ● 4th Qtr</div>
  <div class="a" style="left:329px;top:79px;width:190px">
    <div style="font-size:8px;color:var(--red);margin-bottom:4px">Insert title here</div>
    <p class="tiny" style="margin-bottom:12px">There are many variations of passages of lorem ipsum available, but the majority have suffered alteration in some form, act</p>
    <div style="font-size:8px;color:var(--ink);margin-bottom:4px">Insert title here</div>
    <p class="tiny" style="margin-bottom:12px">There are many variations of passages of lorem ipsum available, but the majority have suffered alteration in some form, act</p>
    <div style="font-size:8px;color:var(--gray);margin-bottom:4px">Insert title here</div>
    <p class="tiny">There are many variations of passages of lorem ipsum available, but the majority have suffered alteration in some form, act</p>
  </div>
  <footer class="ft"><span class="ft-mark">Meridian</span><span class="ft-url">www.meridiangaming-intl.com</span><span class="ft-no">8</span></footer>
</section>

<section class="slide col-r" style="top:1414px">
  <div class="photo" role="img" aria-label="Photo of a roulette table with players in a dark casino" style="left:0;top:0;width:562px;height:316px;background:linear-gradient(120deg,#1d2a30,#3a4c50 45%,#14191c 70%,#2b2422)"></div>
  <div class="a" style="left:38px;top:55px;color:var(--white);font-size:13px">Goals</div>
  <div class="a" style="left:36px;top:90px;width:18px;height:18px;border:1.5px solid var(--white);border-radius:50%"></div>
  <div class="a" style="left:66px;top:86px;width:230px;color:var(--white)"><div style="font-size:6px;letter-spacing:1.5px;font-weight:700">LOREM IPSUM DOLOR</div><p style="font-size:6px;line-height:1.6">Lorem ipsum dolor sit amet, consectetuer adipiscing elit, sed diam nonummy nibh euismod tincidunt ut laoreet dolore magna aliquam erat volutpat.</p></div>
  <div class="a" style="left:38px;top:150px;color:var(--white);font-size:13px">Gaming</div>
  <div class="a" style="left:36px;top:188px;width:18px;height:20px;border:1.5px solid var(--white)"></div>
  <div class="a" style="left:66px;top:184px;width:230px;color:var(--white)"><div style="font-size:6px;letter-spacing:1.5px;font-weight:700">LOREM IPSUM DOLOR</div><p style="font-size:6px;line-height:1.6">Lorem ipsum dolor sit amet, consectetuer adipiscing elit, sed diam nonummy nibh euismod tincidunt ut laoreet dolore magna aliquam erat volutpat.</p></div>
  <div class="a" style="left:316px;top:93px;width:194px;height:118px;background:var(--red);color:var(--white);text-align:center">
    <div class="wordmark" style="font-size:14px;margin-top:34px">Meridian</div>
    <div style="font-size:6px;margin-top:26px">Add your text/ picture here and<br>send it to back</div>
  </div>
</section>

<section class="slide col-l" style="top:1760px">
  <div class="topline"></div><h2 class="title">Infographic Wheel &amp; Mockups</h2>
  <svg class="a" style="left:41px;top:65px" width="182" height="182" viewBox="-91 -91 182 182">
    <path d="M0 0 L0 -91 A91 91 0 0 1 64.3 -64.3Z" fill="#c8101d"/>
    <path d="M0 0 L64.3 -64.3 A91 91 0 0 1 91 0Z" fill="#1f1f1f"/>
    <path d="M0 0 L91 0 A91 91 0 0 1 64.3 64.3Z" fill="#c8101d"/>
    <path d="M0 0 L64.3 64.3 A91 91 0 0 1 0 91Z" fill="#1f1f1f"/>
    <path d="M0 0 L0 91 A91 91 0 0 1 -64.3 64.3Z" fill="#c8101d"/>
    <path d="M0 0 L-64.3 64.3 A91 91 0 0 1 -91 0Z" fill="#1f1f1f"/>
    <path d="M0 0 L-91 0 A91 91 0 0 1 -64.3 -64.3Z" fill="#c8101d"/>
    <path d="M0 0 L-64.3 -64.3 A91 91 0 0 1 0 -91Z" fill="#1f1f1f"/>
    <g fill="#fff"><circle cx="24" cy="-58" r="6"/><circle cx="58" cy="-24" r="6"/><circle cx="58" cy="24" r="6"/><circle cx="24" cy="58" r="6"/><circle cx="-24" cy="58" r="6"/><circle cx="-58" cy="24" r="6"/><circle cx="-58" cy="-24" r="6"/><circle cx="-24" cy="-58" r="6"/></g>
    <circle r="30" fill="#fff"/><circle r="24" fill="#c8101d"/>
  </svg>
  <div class="a" style="left:255px;top:82px;width:150px">
    <p class="tiny" style="margin-bottom:18px">Lorem Ipsum is simply dummy text of the printing and typesetting industry.</p>
    <p class="tiny" style="margin-bottom:18px">Lorem Ipsum is simply dummy text of the printing and typesetting industry.</p>
    <p class="tiny" style="margin-bottom:18px">Lorem Ipsum is simply dummy text of the printing and typesetting industry.</p>
    <p class="tiny">Lorem Ipsum is simply dummy text of the printing and typesetting industry.</p>
  </div>
  <div class="photo" role="img" aria-label="White smartphone mockup" style="left:427px;top:25px;width:105px;height:223px;border-radius:16px;background:#e4e5e8"></div>
  <div class="a" style="left:434px;top:52px;width:91px;height:168px;background:var(--red);color:var(--white);text-align:center;font-size:6px;padding-top:118px">Add your text/ picture here and send it to back</div>
  <footer class="ft"><span class="ft-mark">Meridian</span><span class="ft-url">www.meridiangaming-intl.com</span><span class="ft-no">10</span></footer>
</section>

<section class="slide col-r" style="top:1760px">
  <div class="topline"></div><h2 class="title red">Tables</h2>
  <div class="ic" style="left:506px;top:30px;width:32px;height:32px"><svg viewBox="0 0 16 16"><path d="M2 2h5v5H2zm7 0h5v5H9zM2 9h5v5H2zm7 0h5v5H9z"/></svg></div>
  <table class="tbl">
    <tr><th class="blank"></th><th style="width:90px">Title here</th><th>Numbers</th><th>Value</th><th>Brand</th><th>Quality</th></tr>
    <tr><td class="lab">Content type</td><td>Example one</td><td>3</td><td>33</td><td>New</td><td>15%</td></tr>
    <tr><td class="lab">Content type</td><td>Example two</td><td>6</td><td>45</td><td>New</td><td>60%</td></tr>
    <tr><td class="lab">Content type</td><td>Example three</td><td>6</td><td>67</td><td>New</td><td>67%</td></tr>
    <tr><td class="lab">Content type</td><td>Example four</td><td>9</td><td>94</td><td>New</td><td>22%</td></tr>
    <tr><td class="lab">Content type</td><td>Example five</td><td>2</td><td>50</td><td>New</td><td>15%</td></tr>
    <tr><td class="lab">Content type</td><td>Example six</td><td>1</td><td>90</td><td>New</td><td>89%</td></tr>
    <tr><td class="lab">Content type</td><td>Example seven</td><td>5</td><td>31</td><td>New</td><td>10%</td></tr>
  </table>
  <footer class="ft"><span class="ft-mark">Meridian</span><span class="ft-url">www.meridiangaming-intl.com</span><span class="ft-no">11</span></footer>
</section>

<section class="slide col-l" style="top:2105px;background:var(--white)">
  <div class="sec-tag">SECTION 01</div>
  <div class="sec-word" style="font-size:84px;top:60px;letter-spacing:5px">MANAGEMENT</div>
  <div class="ic" style="left:47px;top:188px;width:35px;height:35px"><svg viewBox="0 0 16 16"><circle cx="8" cy="5" r="3"/><path d="M2 15c0-4 3-6 6-6s6 2 6 6z"/></svg></div>
  <div class="a" style="left:100px;top:180px;width:1px;height:56px;background:var(--line)"></div>
  <p class="a body" style="left:114px;top:183px;width:408px">Lorem ipsum dolor sit amet, consectetuer adipiscing elit, sed diam nonummy nibh euismod tincidunt ut laoreet dolore magna aliquam erat volutpat. Ut wisi enim ad minim veniam, quis nostrud exerci tation ullamcorper suscipit lobortis nisl ut aliquip ex ea commodo consequat. Duis autem vel eum iriure dolor in hendrerit in vulputate velit esse molestie consequat.</p>
  <div class="sec-rule"></div><div class="sec-name">MANAGEMENT</div>
</section>

<section class="slide col-r" style="top:2105px">
  <div class="topline"></div><h2 class="title">Management Process</h2>
  <div class="a" style="left:10px;top:115px;width:542px;height:1px;background:var(--gray)"></div>
  <div class="ic" style="left:38px;top:100px"><svg viewBox="0 0 16 16"><path d="M8 1 14 8 8 15 2 8z"/></svg></div>
  <div class="ic" style="left:129px;top:100px"><svg viewBox="0 0 16 16"><rect x="2" y="4" width="12" height="9"/></svg></div>
  <div class="ic" style="left:220px;top:100px"><svg viewBox="0 0 16 16"><circle cx="8" cy="8" r="6"/></svg></div>
  <div class="ic" style="left:312px;top:100px"><svg viewBox="0 0 16 16"><path d="M3 2h10v3L8 14H5l5-9H3z"/></svg></div>
  <div class="ic" style="left:403px;top:100px"><svg viewBox="0 0 16 16"><circle cx="8" cy="4.5" r="3"/><circle cx="4.5" cy="9.5" r="3"/><circle cx="11.5" cy="9.5" r="3"/><path d="M7 9h2l1 6H6z"/></svg></div>
  <div class="ic" style="left:489px;top:100px"><svg viewBox="0 0 16 16"><path d="M8 15 2 8.5A3.5 3.5 0 0 1 8 4a3.5 3.5 0 0 1 6 4.5z"/></svg></div>
  <div class="a" style="left:16px;top:144px;width:530px;display:flex;justify-content:space-between;text-align:center">
    <div style="width:78px"><div style="font-size:7px;font-weight:700;margin-bottom:6px">LOREM IPSUM</div><p class="tiny">Lorem Ipsum is simply dummy text of the printing and typesetting industry</p></div>
    <div style="width:78px"><div style="font-size:7px;font-weight:700;margin-bottom:6px">LOREM IPSUM</div><p class="tiny">Lorem Ipsum is simply dummy text of the printing and typesetting industry</p></div>
    <div style="width:78px"><div style="font-size:7px;font-weight:700;margin-bottom:6px">LOREM IPSUM</div><p class="tiny">Lorem Ipsum is simply dummy text of the printing and typesetting industry</p></div>
    <div style="width:78px"><div style="font-size:7px;font-weight:700;margin-bottom:6px">LOREM IPSUM</div><p class="tiny">Lorem Ipsum is simply dummy text of the printing and typesetting industry</p></div>
    <div style="width:78px"><div style="font-size:7px;font-weight:700;margin-bottom:6px">LOREM IPSUM</div><p class="tiny">Lorem Ipsum is simply dummy text of the printing and typesetting industry</p></div>
    <div style="width:78px"><div style="font-size:7px;font-weight:700;margin-bottom:6px">LOREM IPSUM</div><p class="tiny">Lorem Ipsum is simply dummy text of the printing and typesetting industry</p></div>
  </div>
  <footer class="ft"><span class="ft-mark">Meridian</span><span class="ft-url">www.meridiangaming-intl.com</span><span class="ft-no">14</span></footer>
</section>

<section class="slide col-l" style="top:2451px">
  <div class="topline"></div><h2 class="title red">Our Team</h2>
  <div class="a" style="left:26px;top:62px;width:510px;display:flex;justify-content:space-around;text-align:center">
    <div style="width:118px"><div role="img" aria-label="Portrait photo of team member" style="width:66px;height:66px;border-radius:50%;background:#b8bbc0;margin:0 auto 10px"></div><div style="font-size:8px;color:var(--red)">Example Name</div><div style="font-size:6.5px;margin-bottom:5px">CEO</div><p class="tiny">There are many variations of passages of lorem ipsum available, but the majority have suffered alteration</p><div style="font-size:7px;color:var(--gray);margin-top:10px">◯ ◯ ◯</div></div>
    <div style="width:118px"><div role="img" aria-label="Portrait photo of team member" style="width:66px;height:66px;border-radius:50%;background:#a9acb1;margin:0 auto 10px"></div><div style="font-size:8px;color:var(--red)">Example Name</div><div style="font-size:6.5px;margin-bottom:5px">Member</div><p class="tiny">There are many variations of passages of lorem ipsum available, but the majority have suffered alteration</p><div style="font-size:7px;color:var(--gray);margin-top:10px">◯ ◯ ◯</div></div>
    <div style="width:118px"><div role="img" aria-label="Portrait photo of team member" style="width:66px;height:66px;border-radius:50%;background:#c3c5c9;margin:0 auto 10px"></div><div style="font-size:8px;color:var(--red)">Example Name</div><div style="font-size:6.5px;margin-bottom:5px">Member</div><p class="tiny">There are many variations of passages of lorem ipsum available, but the majority have suffered alteration</p><div style="font-size:7px;color:var(--gray);margin-top:10px">◯ ◯ ◯</div></div>
    <div style="width:118px"><div role="img" aria-label="Portrait photo of team member" style="width:66px;height:66px;border-radius:50%;background:#b1b4b9;margin:0 auto 10px"></div><div style="font-size:8px;color:var(--red)">Example Name</div><div style="font-size:6.5px;margin-bottom:5px">Support</div><p class="tiny">There are many variations of passages of lorem ipsum available, but the majority have suffered alteration</p><div style="font-size:7px;color:var(--gray);margin-top:10px">◯ ◯ ◯</div></div>
  </div>
  <footer class="ft"><span class="ft-mark">Meridian</span><span class="ft-url">www.meridiangaming-intl.com</span><span class="ft-no">15</span></footer>
</section>

<section class="slide col-r" style="top:2451px">
  <div class="topline"></div><h2 class="title">Analysis Charts</h2>
  <svg class="a" style="left:40px;top:68px" width="88" height="88" viewBox="0 0 88 88"><circle cx="44" cy="44" r="36" fill="#fff" stroke="#e3e4e7" stroke-width="6"/><circle cx="44" cy="44" r="36" fill="none" stroke="#c8101d" stroke-width="6" stroke-dasharray="165 226" transform="rotate(-90 44 44)"/><text x="44" y="50" text-anchor="middle" font-family="Roboto" font-size="18" fill="#262626">73%</text></svg>
  <svg class="a" style="left:40px;top:164px" width="88" height="88" viewBox="0 0 88 88"><circle cx="44" cy="44" r="36" fill="#fff" stroke="#e3e4e7" stroke-width="6"/><circle cx="44" cy="44" r="36" fill="none" stroke="#c8101d" stroke-width="6" stroke-dasharray="113 226" transform="rotate(-90 44 44)"/><text x="44" y="50" text-anchor="middle" font-family="Roboto" font-size="18" fill="#262626">50%</text></svg>
  <div class="a" style="left:141px;top:86px;width:110px"><div style="font-size:7px;font-weight:700;margin-bottom:4px">Analysis 01</div><p class="tiny">Lorem Ipsum is simply dummy text of the printing and typesetting industry</p></div>
  <div class="a" style="left:141px;top:182px;width:110px"><div style="font-size:7px;font-weight:700;margin-bottom:4px">Analysis 02</div><p class="tiny">Lorem Ipsum is simply dummy text of the printing and typesetting industry</p></div>
  <div class="a" style="left:278px;top:70px;width:235px;font-size:7px">
    <div style="display:flex;justify-content:space-between;font-weight:700"><span>Analysis 03</span><span style="font-weight:400">32%</span></div><div class="bar" style="position:relative;width:235px;margin:5px 0 23px"><i style="width:32%"></i></div>
    <div style="display:flex;justify-content:space-between;font-weight:700"><span>Analysis 04</span><span style="font-weight:400">72%</span></div><div class="bar" style="position:relative;width:235px;margin:5px 0 23px"><i style="width:72%;background:#9a9ea4"></i></div>
    <div style="display:flex;justify-content:space-between;font-weight:700"><span>Analysis 05</span><span style="font-weight:400">52%</span></div><div class="bar" style="position:relative;width:235px;margin:5px 0 23px"><i style="width:52%"></i></div>
    <div style="display:flex;justify-content:space-between;font-weight:700"><span>Analysis 06</span><span style="font-weight:400">12%</span></div><div class="bar" style="position:relative;width:235px;margin:5px 0 23px"><i style="width:12%;background:#9a9ea4"></i></div>
    <div style="display:flex;justify-content:space-between;font-weight:700"><span>Analysis 07</span><span style="font-weight:400">60%</span></div><div class="bar" style="position:relative;width:235px;margin:5px 0 0"><i style="width:60%"></i></div>
  </div>
  <footer class="ft"><span class="ft-mark">Meridian</span><span class="ft-url">www.meridiangaming-intl.com</span><span class="ft-no">16</span></footer>
</section>

<section class="slide col-l" style="top:2796px">
  <div class="topline"></div><h2 class="title">Images With Text</h2>
  <div class="photo" role="img" aria-label="Photo of a spinning roulette wheel" style="left:25px;top:51px;width:177px;height:123px;background:linear-gradient(160deg,#3b2418,#6e2a1c 60%,#1b1411)"></div>
  <div class="photo" role="img" aria-label="Photo of casino chip stacks" style="left:211px;top:51px;width:70px;height:123px;background:linear-gradient(160deg,#d9c7a8,#6a4d88 55%,#2a2430)"></div>
  <div class="ic" style="left:299px;top:60px"><svg viewBox="0 0 16 16"><path d="M5 14h7l-1-4 2-2-3-6-4 3-1 4 2 1z"/></svg></div>
  <p class="a body" style="left:299px;top:100px;width:237px;text-align:justify">Lorem ipsum dolor sit amet, consectetuer adipiscing elit, sed diam nonummy nibh euismod tincidunt ut laoreet dolore magna aliquam erat volutpat. Ut wisi enim ad minim veniam, quis nostrud exerci tation ullamcorper suscipit lobortis nisl ut aliquip ex ea commodo consequat.</p>
  <p class="a body" style="left:25px;top:184px;width:256px">Lorem ipsum dolor sit amet, consectetuer adipiscing elit, sed diam nonummy nibh euismod tincidunt ut laoreet dolore magna aliquam erat volutpat. Ut wisi enim ad minim veniam, quis nostrud exerci tation ullamcorper suscipit lobortis nisl ut aliquip ex ea commodo consequat.</p>
  <div class="photo" role="img" aria-label="Photo of red dice on a dark surface" style="left:299px;top:183px;width:165px;height:79px;background:linear-gradient(135deg,#1c1c1c,#5a1a1e 55%,#151515)"></div>
  <div class="photo" role="img" aria-label="Photo of playing cards" style="left:470px;top:183px;width:66px;height:79px;background:linear-gradient(135deg,#f1f1f1,#bdbdbd)"></div>
  <footer class="ft"><span class="ft-mark">Meridian</span><span class="ft-url">www.meridiangaming-intl.com</span><span class="ft-no">17</span></footer>
</section>

<section class="slide col-r" style="top:2796px">
  <div class="topline"></div><h2 class="title">Analysis Infographic</h2>
  <svg class="a" style="left:205px;top:80px" width="152" height="160" viewBox="0 0 152 160" font-family="Roboto" font-size="14" text-anchor="middle">
    <circle cx="76" cy="80" r="16" fill="#bfc2c6"/>
    <g fill="#c8101d"><circle cx="76" cy="32" r="28"/><circle cx="36" cy="76" r="28"/><circle cx="117" cy="76" r="28"/><circle cx="76" cy="120" r="28"/></g>
    <g fill="#fff"><circle cx="76" cy="32" r="19"/><circle cx="36" cy="76" r="19"/><circle cx="117" cy="76" r="19"/><circle cx="76" cy="120" r="19"/></g>
    <g fill="#262626"><text x="76" y="37">S</text><text x="36" y="81">T</text><text x="117" y="81">W</text><text x="76" y="125">O</text></g>
  </svg>
  <div class="a" style="left:21px;top:82px;width:172px;text-align:center"><div style="font-size:6.5px;font-weight:700;color:var(--red);text-align:right">STRENGTH</div><p class="tiny" style="font-size:5.5px">Lorem ipsum dolor sit amet, consectetuer adipiscing elit, sed diam nonummy nibh euismod tincidunt ut laoreet dolore magna aliquam erat</p></div>
  <div class="a" style="left:364px;top:82px;width:176px"><div style="font-size:6.5px;font-weight:700;color:var(--red)">WEAKNESS</div><p class="tiny" style="font-size:5.5px">Lorem ipsum dolor sit amet, consectetuer adipiscing elit, sed diam nonummy nibh euismod tincidunt ut laoreet dolore magna aliquam erat</p></div>
  <div class="a" style="left:21px;top:196px;width:172px;text-align:center"><div style="font-size:6.5px;font-weight:700;color:var(--red);text-align:right">THREAT</div><p class="tiny" style="font-size:5.5px">Lorem ipsum dolor sit amet, consectetuer adipiscing elit, sed diam nonummy nibh euismod tincidunt ut laoreet dolore magna aliquam erat</p></div>
  <div class="a" style="left:364px;top:196px;width:176px"><div style="font-size:6.5px;font-weight:700;color:var(--red)">OPPORTUNITY</div><p class="tiny" style="font-size:5.5px">Lorem ipsum dolor sit amet, consectetuer adipiscing elit, sed diam nonummy nibh euismod tincidunt ut laoreet dolore magna aliquam erat</p></div>
  <footer class="ft"><span class="ft-mark">Meridian</span><span class="ft-url">www.meridiangaming-intl.com</span><span class="ft-no">18</span></footer>
</section>

<section class="slide col-l" style="top:3142px">
  <div class="topline"></div><h2 class="title">Text Information</h2>
  <div class="ic" style="left:47px;top:80px;color:#fff;font-size:11px">1</div>
  <div class="ic" style="left:47px;top:145px;color:#fff;font-size:11px">2</div>
  <div class="ic" style="left:47px;top:210px;color:#fff;font-size:11px">3</div>
  <div class="ic" style="left:307px;top:80px;color:#fff;font-size:11px">4</div>
  <div class="ic" style="left:307px;top:145px;color:#fff;font-size:11px">5</div>
  <div class="ic" style="left:307px;top:210px;color:#fff;font-size:11px">6</div>
  <div class="a" style="left:88px;top:80px;width:180px"><div style="font-size:6px;letter-spacing:1.5px;font-weight:700;color:var(--red);margin-bottom:4px">TEXT INFORMATION</div><p class="tiny">Lorem ipsum dolor sit amet, consectetuer adipiscing elit, sed diam nonummy nibh euismod tincidunt ut laoreet dolore magna</p></div>
  <div class="a" style="left:88px;top:145px;width:180px"><div style="font-size:6px;letter-spacing:1.5px;font-weight:700;color:var(--red);margin-bottom:4px">TEXT INFORMATION</div><p class="tiny">Lorem ipsum dolor sit amet, consectetuer adipiscing elit, sed diam nonummy nibh euismod tincidunt ut laoreet dolore magna</p></div>
  <div class="a" style="left:88px;top:210px;width:180px"><div style="font-size:6px;letter-spacing:1.5px;font-weight:700;color:var(--red);margin-bottom:4px">TEXT INFORMATION</div><p class="tiny">Lorem ipsum dolor sit amet, consectetuer adipiscing elit, sed diam nonummy nibh euismod tincidunt ut laoreet dolore magna</p></div>
  <div class="a" style="left:348px;top:80px;width:180px"><div style="font-size:6px;letter-spacing:1.5px;font-weight:700;color:var(--red);margin-bottom:4px">TEXT INFORMATION</div><p class="tiny">Lorem ipsum dolor sit amet, consectetuer adipiscing elit, sed diam nonummy nibh euismod tincidunt ut laoreet dolore magna</p></div>
  <div class="a" style="left:348px;top:145px;width:180px"><div style="font-size:6px;letter-spacing:1.5px;font-weight:700;color:var(--red);margin-bottom:4px">TEXT INFORMATION</div><p class="tiny">Lorem ipsum dolor sit amet, consectetuer adipiscing elit, sed diam nonummy nibh euismod tincidunt ut laoreet dolore magna</p></div>
  <div class="a" style="left:348px;top:210px;width:180px"><div style="font-size:6px;letter-spacing:1.5px;font-weight:700;color:var(--red);margin-bottom:4px">TEXT INFORMATION</div><p class="tiny">Lorem ipsum dolor sit amet, consectetuer adipiscing elit, sed diam nonummy nibh euismod tincidunt ut laoreet dolore magna</p></div>
  <footer class="ft"><span class="ft-mark">Meridian</span><span class="ft-url">www.meridiangaming-intl.com</span><span class="ft-no">19</span></footer>
</section>

<section class="slide col-r" style="top:3142px">
  <div class="topline"></div><h2 class="title">Infograpic</h2>
  <svg class="a" style="left:190px;top:70px" width="240" height="180" viewBox="0 0 240 180" font-family="Roboto" font-size="13" text-anchor="middle">
    <g fill="#c8101d"><circle cx="86" cy="52" r="40"/><circle cx="126" cy="122" r="40"/><circle cx="45" cy="122" r="40"/></g>
    <g fill="#fff"><circle cx="86" cy="52" r="26"/><circle cx="126" cy="122" r="26"/><circle cx="45" cy="122" r="26"/></g>
    <circle cx="86" cy="98" r="9" fill="#262626"/>
    <g fill="#262626"><text x="86" y="57">A</text><text x="126" y="127">B</text><text x="45" y="127">C</text></g>
    <g stroke="#262626" stroke-width=".8" stroke-dasharray="2 2" fill="none"><path d="M120 30 L178 18"/><path d="M160 140 L204 136"/></g>
  </svg>
  <div class="a" style="left:362px;top:80px;width:16px;height:16px;border-radius:50%;background:#262626;color:#fff;font-size:7px;text-align:center;line-height:16px">A</div>
  <div class="a" style="left:384px;top:80px;width:160px"><div style="font-size:6px;letter-spacing:1.5px;font-weight:700;color:var(--red);margin-bottom:3px">TEXT INFORMATION</div><p class="tiny">Lorem ipsum dolor sit amet, consectetuer adipiscing elit, sed diam nonummy nibh euismod tincidunt ut laoreet dolore magna</p></div>
  <div class="a" style="left:388px;top:198px;width:16px;height:16px;border-radius:50%;background:#262626;color:#fff;font-size:7px;text-align:center;line-height:16px">B</div>
  <div class="a" style="left:410px;top:198px;width:140px"><div style="font-size:6px;letter-spacing:1.5px;font-weight:700;color:var(--red);margin-bottom:3px">TEXT INFORMATION</div><p class="tiny">Lorem ipsum dolor sit amet, consectetuer adipiscing elit, sed diam nonummy nibh euismod tincidunt ut laoreet dolore magna</p></div>
  <div class="a" style="left:166px;top:114px;width:16px;height:16px;border-radius:50%;background:#262626;color:#fff;font-size:7px;text-align:center;line-height:16px">C</div>
  <div class="a" style="left:30px;top:116px;width:130px;text-align:right"><div style="font-size:6px;letter-spacing:1.5px;font-weight:700;color:var(--red);margin-bottom:3px">TEXT INFORMATION</div><p class="tiny">Lorem ipsum dolor sit amet, consectetuer adipiscing elit, sed diam nonummy nibh euismod tincidunt ut laoreet dolore magna</p></div>
  <footer class="ft"><span class="ft-mark">Meridian</span><span class="ft-url">www.meridiangaming-intl.com</span><span class="ft-no">20</span></footer>
</section>

<section class="slide col-l" style="top:3488px">
  <div class="topline"></div><h2 class="title">Infograpic</h2>
  <svg class="a" style="left:0;top:0" width="562" height="316" viewBox="0 0 562 316">
    <g stroke="#262626" stroke-width=".8" stroke-dasharray="2 2" fill="none"><path d="M200 98 H230 L232 130"/><path d="M200 155 H218"/><path d="M200 228 H230 L232 196"/><path d="M362 98 H338 L336 130"/><path d="M362 155 H352"/><path d="M362 228 H338 L336 196"/></g>
    <circle cx="285" cy="163" r="67" fill="#fff" stroke="#262626" stroke-width="1.2"/>
    <circle cx="285" cy="163" r="56" fill="none" stroke="#c8101d" stroke-width="3"/>
    <text x="285" y="167" text-anchor="middle" font-family="Roboto" font-weight="700" font-size="12" letter-spacing="2" fill="#c8101d">MERIDIAN</text>
  </svg>
  <div class="ic" style="left:100px;top:68px"><svg viewBox="0 0 16 16"><rect x="2" y="3" width="12" height="10"/></svg></div>
  <div class="ic" style="left:100px;top:140px"><svg viewBox="0 0 16 16"><circle cx="8" cy="8" r="6"/></svg></div>
  <div class="ic" style="left:100px;top:213px"><svg viewBox="0 0 16 16"><path d="M8 1 14 8 8 15 2 8z"/></svg></div>
  <div class="ic" style="left:448px;top:68px"><svg viewBox="0 0 16 16"><path d="M3 2h10v3L8 14H5l5-9H3z"/></svg></div>
  <div class="ic" style="left:448px;top:140px"><svg viewBox="0 0 16 16"><rect x="3" y="3" width="10" height="10"/></svg></div>
  <div class="ic" style="left:448px;top:213px"><svg viewBox="0 0 16 16"><circle cx="8" cy="5" r="3"/><path d="M2 15c0-4 3-6 6-6s6 2 6 6z"/></svg></div>
  <div class="a" style="left:140px;top:74px;width:64px"><div style="font-size:6px;font-weight:700;color:var(--red)">LOREM IPSUM</div><p class="tiny" style="font-size:5px">Lorem ipsum dolor sit amet, cons adipiscing elit</p></div>
  <div class="a" style="left:140px;top:146px;width:64px"><div style="font-size:6px;font-weight:700;color:var(--red)">LOREM IPSUM</div><p class="tiny" style="font-size:5px">Lorem ipsum dolor sit amet, cons adipiscing elit</p></div>
  <div class="a" style="left:140px;top:219px;width:64px"><div style="font-size:6px;font-weight:700;color:var(--red)">LOREM IPSUM</div><p class="tiny" style="font-size:5px">Lorem ipsum dolor sit amet, cons adipiscing elit</p></div>
  <div class="a" style="left:366px;top:74px;width:72px;text-align:right"><div style="font-size:6px;font-weight:700;color:var(--red)">LOREM IPSUM</div><p class="tiny" style="font-size:5px">Lorem ipsum dolor sit amet, cons adipiscing elit</p></div>
  <div class="a" style="left:366px;top:146px;width:72px;text-align:right"><div style="font-size:6px;font-weight:700;color:var(--red)">LOREM IPSUM</div><p class="tiny" style="font-size:5px">Lorem ipsum dolor sit amet, cons adipiscing elit</p></div>
  <div class="a" style="left:366px;top:219px;width:72px;text-align:right"><div style="font-size:6px;font-weight:700;color:var(--red)">LOREM IPSUM</div><p class="tiny" style="font-size:5px">Lorem ipsum dolor sit amet, cons adipiscing elit</p></div>
  <footer class="ft"><span class="ft-mark">Meridian</span><span class="ft-url">www.meridiangaming-intl.com</span><span class="ft-no">21</span></footer>
</section>

<section class="slide col-r" style="top:3488px">
  <div class="topline"></div><h2 class="title">Locations — In Austria</h2>
  <div class="photo" role="img" aria-label="Map of Austria with regions and red location pins" style="left:18px;top:97px;width:281px;height:167px;background:linear-gradient(135deg,#e6e7ea,#d8dadd 60%,#e6e7ea)"></div>
  <div class="ic" style="left:316px;top:72px"><svg viewBox="0 0 16 16"><path d="M8 15s5-5 5-9a5 5 0 0 0-10 0c0 4 5 9 5 9zm0-7a2 2 0 1 1 0-4 2 2 0 0 1 0 4z"/></svg></div>
  <div class="a" style="left:356px;top:76px;width:170px"><div style="font-size:7px;font-weight:700;color:var(--red);margin-bottom:2px">AUSTRIA editable map</div><p class="tiny" style="font-size:5px">Lorem ipsum dolor sit amet, consectetuer adipiscing elit</p></div>
  <div class="a" style="left:316px;top:112px;width:1px;height:150px;background:var(--line)"></div>
  <svg class="a" style="left:340px;top:145px" width="80" height="80" viewBox="0 0 80 80"><circle cx="40" cy="40" r="34" fill="#fff" stroke="#e3e4e7" stroke-width="5"/><circle cx="40" cy="40" r="34" fill="none" stroke="#c8101d" stroke-width="5" stroke-dasharray="107 214" transform="rotate(-90 40 40)"/><text x="40" y="46" text-anchor="middle" font-family="Roboto" font-size="17" fill="#262626">50%</text></svg>
  <div class="a" style="left:437px;top:152px;width:110px"><div style="font-size:7px;font-weight:700;margin-bottom:3px">INFOGRAPHICS</div><p class="tiny">Lorem Ipsum is simply dummy text of the printing and typesetting industry</p></div>
  <footer class="ft"><span class="ft-mark">Meridian</span><span class="ft-url">www.meridiangaming-intl.com</span><span class="ft-no">22</span></footer>
</section>

<section class="slide col-l" style="top:3833px">
  <div class="topline"></div><h2 class="title">Locations — International</h2>
  <div class="photo" role="img" aria-label="World map with red location pins" style="left:153px;top:49px;width:386px;height:211px;background:linear-gradient(135deg,#e8e9ec,#dcdee1 55%,#e8e9ec)"></div>
  <div class="ic" style="left:109px;top:70px"><svg viewBox="0 0 16 16"><path d="M8 15s5-5 5-9a5 5 0 0 0-10 0c0 4 5 9 5 9zm0-7a2 2 0 1 1 0-4 2 2 0 0 1 0 4z"/></svg></div>
  <div class="a" style="left:25px;top:108px;width:120px"><div style="font-size:6.5px;font-weight:700;color:var(--red);margin-bottom:2px">World editable map</div><p class="tiny" style="font-size:5px">Lorem ipsum dolor sit amet, consectetuer adipiscing elit</p></div>
  <div class="a" style="left:25px;top:148px;width:110px;font-size:5px;font-weight:700">
    <div style="display:flex;justify-content:space-between"><span>MEN</span><span style="font-weight:400">70%</span></div><div class="bar" style="position:relative;width:110px;height:3px;margin:3px 0 8px"><i style="width:70%;height:3px"></i></div>
    <div style="display:flex;justify-content:space-between"><span>WOMEN</span><span style="font-weight:400">30%</span></div><div class="bar" style="position:relative;width:110px;height:3px;margin-top:3px"><i style="width:30%;height:3px;background:#5f646b"></i></div>
  </div>
  <footer class="ft"><span class="ft-mark">Meridian</span><span class="ft-url">www.meridiangaming-intl.com</span><span class="ft-no">23</span></footer>
</section>

<section class="slide col-r" style="top:3833px">
  <h2 class="title" style="top:20px">Free Vector Icon Links Available</h2>
  <div class="photo" role="img" aria-label="Grid of red line icons for business and gaming topics" style="left:26px;top:58px;width:519px;height:228px;background:linear-gradient(135deg,#f3d6d8,#eec3c6 50%,#f3d6d8)"></div>
</section>

<section class="slide col-l" style="top:4179px;background:var(--red)">
  <div class="mark-disc" style="left:340px;top:66px;width:200px;height:200px"><span class="wordmark" style="color:var(--red);font-size:22px">Meridian</span></div>
  <div class="a" style="left:33px;top:143px;color:var(--white);font-size:17px">GET IN TOUCH</div>
  <div class="a" style="left:33px;top:182px;color:var(--white);font-size:7px;line-height:31px">
    <div><span style="display:inline-block;width:12px;height:12px;border:1px solid #fff;border-radius:50%;vertical-align:middle;margin-right:14px"></span>www.meridiangaming-intl.com</div>
    <div><span style="display:inline-block;width:12px;height:12px;border:1px solid #fff;border-radius:50%;vertical-align:middle;margin-right:14px"></span>+1 234 567 890</div>
    <div><span style="display:inline-block;width:12px;height:12px;border:1px solid #fff;vertical-align:middle;margin-right:14px"></span>info@meridiangaming-intl.com</div>
    <div><span style="display:inline-block;width:12px;height:12px;border:1px solid #fff;border-radius:50%;vertical-align:middle;margin-right:14px"></span>Add Your Address, street, road , here</div>
  </div>
</section>

<section class="slide col-r" style="top:4179px;background:var(--white)">
  <div class="a wordmark" style="left:0;right:0;top:138px;text-align:center;color:var(--red);font-size:38px">Meridian</div>
</section>

</body>
</html>
```